Motorcycle Shop Business Card

New business card for Motorcycle repair and customization shop.Business name: Steel Raven Chris Morris443-865-5190, 2817 Orchard Lane Kestrel Falls, PA 17098. www.dale@steelravencustoms.example. I uploaded some motorcycle images and logo and a couple of our calendar shoots. They do not have to be used on card just examples of some of our work and past graphic work.
We work on Torvald Brennan and Custom Built Motorcycles.

Looking for front and back design

Target Market(s)

Motorcycle owners

```html
<!DOCTYPE html>
<html lang="en">
<head>
<meta charset="utf-8">
<title>Steel Raven Customs – Business Card</title>
<link rel="stylesheet" href="https://fonts.googleapis.com/css2?family=Patrick+Hand+SC&display=swap">
<style>
  :root {
    --backdrop: #141414;
    --card-dark: #222222;
    --card-dark-edge: #1a1a1a;
    --card-light: #ffffff;
    --ink-light: #ffffff;
    --ink-dark: #111111;
    --hand: "Patrick Hand SC", cursive;
  }
  html, body {
    margin: 0;
    padding: 0;
    width: 1200px;
    height: 897px;
    overflow: hidden;
    background: var(--backdrop);
  }
  .canvas {
    position: relative;
    width: 1200px;
    height: 897px;
    font-family: var(--hand);
  }
  .card {
    position: absolute;
    left: 303px;
    width: 590px;
    height: 338px;
    overflow: hidden;
    box-shadow: 0 6px 14px rgba(0, 0, 0, 0.6);
  }
  .card--front {
    top: 92px;
    background: linear-gradient(160deg, #2c2c2c 0%, var(--card-dark) 45%, var(--card-dark-edge) 100%);
  }
  .card--back {
    top: 470px;
    background: linear-gradient(160deg, #262626 0%, var(--card-dark) 50%, var(--card-dark-edge) 100%);
  }
  .logo-panel {
    position: absolute;
    left: 0;
    top: 0;
    width: 299px;
    height: 338px;
    background: var(--card-light);
    display: flex;
    align-items: center;
    justify-content: center;
  }
  .wordmark {
    text-align: center;
    line-height: 0.95;
    font-weight: 400;
    text-transform: uppercase;
  }
  .wordmark--dark { color: var(--ink-dark); font-size: 38px; }
  .wordmark--light { color: var(--ink-light); font-size: 58px; }
  .wordmark span { display: block; }
  .card--back .wordmark {
    position: absolute;
    left: 0;
    right: 0;
    top: 50%;
    transform: translateY(-44%);
  }
  .contact {
    position: absolute;
    left: 333px;
    top: 0;
    color: var(--ink-light);
    text-transform: uppercase;
  }
  .contact__name {
    position: absolute;
    top: 50px;
    margin: 0;
    font-size: 38px;
    font-weight: 400;
    line-height: 1;
    white-space: nowrap;
    letter-spacing: 0.5px;
  }
  .contact__line {
    position: absolute;
    margin: 0;
    font-size: 16px;
    line-height: 1.2;
    white-space: nowrap;
  }
  .contact__line--phone { top: 145px; }
  .contact__line--email { top: 179px; }
  .contact__line--street { top: 239px; }
  .contact__line--city { top: 273px; }
</style>
</head>
<body>
  <main class="canvas">
    <section class="card card--front" aria-label="Business card front">
      <div class="logo-panel">
        <div class="wordmark wordmark--dark">
          <span>Steel Raven</span>
          <span>Customs</span>
        </div>
      </div>
      <div class="contact">
        <h1 class="contact__name">Dale Fenwick</h1>
        <p class="contact__line contact__line--phone">Phone: 410-372-6648</p>
        <p class="contact__line contact__line--email">dale@steelravencustoms.example</p>
        <p class="contact__line contact__line--street">2817 Orchard Lane Kestrel Falls,</p>
        <p class="contact__line contact__line--city">PA 17098</p>
      </div>
    </section>

    <section class="card card--back" aria-label="Business card back">
      <div class="wordmark wordmark--light">
        <span>Steel Raven</span>
        <span>Customs</span>
      </div>
    </section>
  </main>
</body>
</html>
```